Brindle Yard Care. The best in the biz

I run a lawn care service that offers full service mowing. 100% satisfaction guarantee. Fast, Friendly, quality service "I am your lawns best friend" I cut residential lawns. I offer a mow package that includes trimming, edging and clean up. Prices very from 20 dollars to 75. I want my logo to stand out. Free estimates

Target Market(s)

Home owners

Industry/Entity Type

Landscaping

Contact Information for Business Card

482-615-0273 tomkerl47@quillmail.net Dorian. Brindle Yard care

Colors
f37122
9bcb3c
cadf82

Requirements
Must have
• Company name.
• Phone number
• Email
• My services
• images
Nice to have
• A sun that is growing grass.
Should not have
• Incorrect information

```html
<!DOCTYPE html>
<html lang="en">
<head>
<meta charset="utf-8">
<title>Brindle Yard Care – Business Card</title>
<link rel="stylesheet" href="https://fonts.googleapis.com/css2?family=Open+Sans:wght@400;600&display=swap">
<style>
  :root {
    --stage: #d6d6d4;
    --card-dark: #0e0e0e;
    --card-mid: #1d1d1d;
    --lime: #9bcb3c;
    --sun: #f37122;
    --pale-lime: #cadf82;
    --ink-light: #f2f2f2;
    --rule: #2e2e2e;
  }
  * { box-sizing: border-box; margin: 0; padding: 0; }
  html, body { width: 1200px; height: 900px; overflow: hidden; }
  body {
    background: var(--stage);
    font-family: "Open Sans", Arial, sans-serif;
    position: relative;
  }
  .card {
    position: absolute;
    left: 320px;
    width: 560px;
    height: 320px;
    background: radial-gradient(ellipse at 60% 40%, var(--card-mid), var(--card-dark) 75%);
    color: var(--lime);
  }
  .card--back { top: 90px; }
  .card--front { top: 490px; }

  /* back side */
  .brand-mark {
    position: absolute;
    top: 62px;
    left: 0; right: 0;
    display: flex;
    align-items: center;
    justify-content: center;
    gap: 12px;
  }
  .brand-mark__dot {
    width: 22px; height: 22px;
    border-radius: 50%;
    background: var(--sun);
  }
  .brand-mark__name {
    font-size: 24px;
    font-weight: 600;
    color: var(--lime);
  }
  .taglines {
    position: absolute;
    top: 150px;
    left: 0; right: 0;
    text-align: center;
    list-style: none;
    font-size: 17px;
    font-weight: 600;
    line-height: 31px;
  }

  /* front side */
  .front__dot {
    position: absolute;
    top: 44px; left: 392px;
    width: 22px; height: 22px;
    border-radius: 50%;
    background: var(--sun);
  }
  .front__person {
    position: absolute;
    top: 106px; left: 48px;
    font-size: 18px;
    font-weight: 600;
    letter-spacing: 0.5px;
  }
  .front__company {
    position: absolute;
    top: 86px; right: 40px;
    font-size: 34px;
    font-weight: 400;
    letter-spacing: 0.5px;
  }
  .front__rule {
    position: absolute;
    top: 146px; left: 150px; right: 40px;
    height: 1px;
    background: var(--rule);
  }
  .contact {
    position: absolute;
    top: 206px; right: 40px;
    list-style: none;
    text-align: right;
    color: var(--ink-light);
    font-size: 17px;
    line-height: 26px;
  }
  .contact__item { display: flex; align-items: center; justify-content: flex-end; gap: 10px; }
  .contact__icon { width: 14px; height: 14px; fill: var(--lime); }
</style>
</head>
<body>

<section class="card card--back">
  <div class="brand-mark">
    <span class="brand-mark__dot"></span>
    <span class="brand-mark__name">Brindle Yard Care</span>
  </div>
  <ul class="taglines">
    <li>100% satisfaction guarantee.</li>
    <li>Fast, Friendly, Quality Service</li>
    <li>I am your lawns best friend</li>
  </ul>
</section>

<section class="card card--front">
  <span class="front__dot"></span>
  <p class="front__person">DORIAN</p>
  <h1 class="front__company">Brindle Yard Care</h1>
  <div class="front__rule"></div>
  <ul class="contact">
    <li class="contact__item">482-615-0273
      <svg class="contact__icon" viewBox="0 0 24 24" aria-hidden="true"><path d="M6.6 10.8a15.1 15.1 0 0 0 6.6 6.6l2.2-2.2a1 1 0 0 1 1-.25 11.4 11.4 0 0 0 3.6.57 1 1 0 0 1 1 1V20a1 1 0 0 1-1 1A17 17 0 0 1 3 4a1 1 0 0 1 1-1h3.5a1 1 0 0 1 1 1c0 1.25.2 2.45.57 3.57a1 1 0 0 1-.25 1z"/></svg>
    </li>
    <li class="contact__item">tomkerl47@quillmail.net
      <svg class="contact__icon" viewBox="0 0 24 24" aria-hidden="true"><path d="M2 5h20v14H2z M2 5l10 8 10-8" fill="none" stroke="#9bcb3c" stroke-width="2"/></svg>
    </li>
  </ul>
</section>

</body>
</html>
```